I need a book cover for a 6x9 book. The front cover information (title and author) is below, and the back cover information will be given to the winning designer. I am wanting something vibrant and bright, and I am open to your creativity, but I do not want any pictures of people on the cover. Save room for the barcode on the back cover.
Title:
Psst! Then Where?
Open Doors, Warm Rooms: Ideas for Lively Evenings Ahead
Author:
Derrion Platt

```html
<!DOCTYPE html>
<html lang="en">
<head>
<meta charset="utf-8">
<title>Psst! Then Where? — Derrion Platt</title>
<link href="https://fonts.googleapis.com/css2?family=Fredoka:wght@700&family=Montserrat:wght@600;900&display=swap" rel="stylesheet">
<style>
  :root {
    --backdrop: #ececec;
    --paper: #ffffff;
    --ink-grey: #4a4a4a;
    --orange-light: #f08f30;
    --orange-deep: #e8622a;
    --title-shadow: #b63f1e;
    --sub-amber: #f29424;
    --sub-red: #e8552a;
  }
  html, body {
    margin: 0;
    width: 1200px;
    height: 1200px;
    overflow: hidden;
    background: var(--backdrop);
  }
  .stage {
    width: 1200px;
    height: 1200px;
    display: flex;
    align-items: center;
    justify-content: center;
  }
  .cover {
    position: relative;
    width: 700px;
    height: 1050px;
    background: var(--paper);
    box-shadow: 0 6px 24px rgba(0,0,0,0.08);
  }
  .author {
    position: absolute;
    top: 80px;
    left: 0;
    right: 0;
    margin: 0;
    text-align: center;
    font-family: "Montserrat", sans-serif;
    font-weight: 600;
    font-size: 32px;
    letter-spacing: 3px;
    color: var(--ink-grey);
  }
  .bubble-art {
    position: absolute;
    top: 150px;
    left: 70px;
    width: 560px;
    height: 600px;
    border-radius: 42% 42% 40% 40% / 36% 36% 44% 44%;
    background: linear-gradient(180deg, var(--orange-light) 0%, var(--orange-light) 50%, var(--orange-deep) 62%, var(--orange-deep) 100%);
  }
  .title {
    position: absolute;
    top: 250px;
    left: 70px;
    width: 560px;
    margin: 0;
    text-align: center;
    font-family: "Montserrat", sans-serif;
    font-weight: 900;
    font-size: 100px;
    line-height: 1.02;
    color: var(--paper);
    text-transform: uppercase;
    text-shadow: 6px 6px 0 var(--title-shadow);
  }
  .title span { display: block; }
  .subtitle {
    position: absolute;
    top: 830px;
    left: 0;
    right: 0;
    margin: 0;
    text-align: center;
    font-family: "Fredoka", sans-serif;
    font-weight: 700;
    text-transform: uppercase;
    line-height: 1.1;
  }
  .subtitle .lead {
    display: block;
    font-size: 40px;
    color: var(--sub-amber);
  }
  .subtitle .tail {
    display: block;
    font-size: 28px;
    color: var(--sub-red);
  }
</style>
</head>
<body>
  <main class="stage">
    <section class="cover">
      <p class="author">DERRION PLATT</p>

      <div class="bubble-art" role="img" aria-label="Glossy orange speech bubble illustration with a small bird perched on top and a bird flying below its tail"></div>

      <h1 class="title">
        <span>Psst!</span>
        <span>Then</span>
        <span>Where?</span>
      </h1>

      <p class="subtitle">
        <span class="lead">Open Doors, Warm Rooms:</span>
        <span class="tail">Ideas for Lively Evenings Ahead</span>
      </p>
    </section>
  </main>
</body>
</html>
```